2018 - 2019 Academic Program & Schedule ofEvents

10 page booklet listing upcoming courses for Sept 2018- May 2019
Program guide showing members what the courses are for the upcoming year.
It gives the course description & learning objectives & CE credits offered for each lecture. Also gives date, time location, intended participants, course description & learning objectives

Please use the RVMK 2016-2017 & 2017-2018 program guides as reference. We don't want to use any actual photo of Hollowell, we would like something more modern and cleaner look like the above mentioned program guides.

Target Market(s)

Dentist

Industry/Entity Type

Dental

Font styles to use
Serif
Script

Colors
f37122

Requirements
Must have
• Must have our logo on front & back
• & "TRIM logo on back
• Table of contents, Course title, Date, location, intended audience, Time, Speaker's name & Title
Nice to have
• Marcus Hollowell quote

```html
<!DOCTYPE html>
<html lang="en">
<head>
<meta charset="utf-8">
<title>Director's Letter</title>
<link rel="stylesheet" href="https://fonts.googleapis.com/css2?family=EB+Garamond:ital,wght@0,400;0,700;1,400&display=swap">
<style>
  :root {
    --backdrop: #ece7e1;
    --paper: #ffffff;
    --ink: #2f2c2a;
    --portrait-dark: #7b3e1b;
    --portrait-mid: #b8704a;
    --portrait-light: #eab797;
  }
  * { box-sizing: border-box; margin: 0; padding: 0; }
  html, body {
    width: 1200px; height: 1200px; overflow: hidden;
    background: var(--backdrop);
  }
  .page {
    position: absolute; left: 211px; top: 30px;
    width: 777px; height: 1140px;
    background: var(--paper);
    display: flex;
    box-shadow: 0 6px 18px rgba(0,0,0,0.18);
  }
  .portrait {
    width: 368px; height: 100%;
    background:
      radial-gradient(ellipse 70% 45% at 55% 40%, var(--portrait-light) 0%, var(--portrait-mid) 55%, transparent 85%),
      linear-gradient(180deg, var(--portrait-mid) 0%, var(--portrait-dark) 70%, #6a3416 100%);
  }
  .letter {
    flex: 1;
    padding: 48px 40px 0 41px;
    font-family: "EB Garamond", Garamond, serif;
    font-size: 15.4px;
    line-height: 19.4px;
    color: var(--ink);
  }
  .letter p { text-align: justify; margin-bottom: 19.4px; }
  .letter .salutation { text-align: left; }
  .letter strong { font-weight: 700; }
  .signoff { text-align: left; }
  .signoff .title { font-style: italic; }
</style>
</head>
<body>
  <article class="page">
    <div class="portrait" role="img" aria-label="Tinted portrait photograph of Marcus Hollowell"></div>
    <section class="letter">
      <p class="salutation">Dear Colleagues,</p>
      <p>The <strong>Rivermark Group For Dental Excellence</strong> has now reached our 10th anniversary. We have kept to our mission of excellence in dental education. We have taken a stepwise approach, always building on the dentistry we have learned from educators that are leaders in their fields and from each other. We are continuing on with this tenet.</p>
      <p>Our program is designed to include the elements of the complete clinician. Over the years we have brought in speakers for the single tooth patient's needs to understanding the sequencing and segmenting of complex cases. We have answered questions about treatment of the medically compromised patient, the oral effects of systemic medication, medical emergencies, occlusion, TMD, endodontic and periodontal therapy. As dentistry has progressed into the digital era, so have we. There are lecture, hands-on, and seminar style presentations. Finally we bring it all together in our case presentation seminars.</p>
      <p>The members design the curriculum. We do this through focus groups and feedback questionnaires. Every course is evaluated and suggestions are made for the future. The directors for the Harborline Study Clubs submit these reviews and promote only the best speakers to draw from. Many of them are show-cased at their annual Harborline Club Symposium.</p>
      <p>As a member of the <strong>Rivermark Group For Dental Excellence</strong> you are also a member of the <strong>Harborline Study Club</strong>. With your tuition you will receive a quarterly journal, online access to their network of information and resources. We have gained recognition by the Guild of General Dentistry, TRIM/ NDO and the Eastbrook State Board of Dentistry as a provider for continuing education.</p>
      <p>Our program will continue to be designed for a selfless sharing of knowledge and member participation that fulfill the needs of the doctors and their offices. It is gratifying to serve as your director of the study club. I encourage you to join us and share what we are building.</p>
      <p class="signoff">Warm regards,<br>Daniel R. Ashford, DMD<br><span class="title">Director, Rivermark Group For Dental Excellence</span></p>
    </section>
  </article>
</body>
</html>
```